Feral Tundra, a 3d voxel survival video game needs a card for gaming conventions

I am the lead developer for Feral Tundra http://www.FeralTundra.example and need a business card to hand out at an indie gaming convention
The card would need to include the game name, website url, my name, position (Lead Developer), e-mail and phone number
The game is a 3d, voxel (with smooth terrain) based survival game with guns and wildlife. The main icon of the game would likely be a grizzly bear but I am willing to accept other designs too.
Attached is a media kit for the game with some images you can use but don't have to its just what little art I can provide. Anything on the website or from the video game can also be used. unrelated art can also be used.
Target Market(s)
Indie Developers/publishers at conferences
Industry/Entity Type
Games
Contact Information for Business Card
Name: Corin Wexford
Position: Lead Developer
E-mail: Gray_Lanterns@mailnest.example
Phone number: 555-372-9186
Look and feel

```html
<!DOCTYPE html>
<html lang="en">
<head>
<meta charset="utf-8">
<title>Feral Tundra – Business Card</title>
<link rel="stylesheet" href="https://fonts.googleapis.com/css2?family=Rubik+Dirt&family=Lato:wght@400;700&display=swap">
<style>
  :root {
    --stage: #ece7e2;
    --card-orange: #f7990b;
    --tag-black: #0c0c0c;
    --tag-text: #ffffff;
    --title-dark: #3a2216;
    --panel-frame: #f5a11c;
    --panel-gap: #1b1f1c;
    --corner-black: #0a0a0a;
    --white: #ffffff;
  }
  * { box-sizing: border-box; margin: 0; padding: 0; }
  html, body { width: 1200px; height: 1200px; overflow: hidden; }
  body {
    background: var(--stage);
    position: relative;
    font-family: "Lato", Arial, sans-serif;
  }
  .card {
    position: absolute;
    left: 127px;
    width: 945px;
    height: 540px;
    overflow: hidden;
    box-shadow: 0 6px 18px rgba(0,0,0,0.18);
  }
  .card--front { top: 30px; background: var(--card-orange); }
  .card--back  { top: 630px; background: var(--panel-gap); }

  /* Front */
  .game-title {
    position: absolute;
    left: 70px; top: 400px;
    font-family: "Lato", Arial, sans-serif;
    font-weight: 700;
    font-size: 60px;
    line-height: 1;
    color: var(--title-dark);
    white-space: nowrap;
  }
  .feature-tags {
    position: absolute;
    right: 60px; top: 95px;
    display: flex;
    flex-direction: column;
    align-items: flex-end;
    gap: 12px;
  }
  .feature-tag {
    background: var(--tag-black);
    color: var(--tag-text);
    font-family: "Rubik Dirt", "Impact", sans-serif;
    font-size: 38px;
    line-height: 1;
    padding: 9px 26px 10px;
  }
  .byline {
    position: absolute;
    right: 70px; bottom: 72px;
    font-family: "Rubik Dirt", "Impact", sans-serif;
    font-size: 30px;
    line-height: 1;
    color: var(--white);
    white-space: nowrap;
  }

  /* Back */
  .screens { position: absolute; inset: 0; width: 945px; height: 540px; }
  .mini-brand {
    position: absolute;
    right: 18px; top: 30px;
    font-family: "Lato", Arial, sans-serif;
    font-weight: 700;
    font-size: 26px;
    line-height: 1;
    color: var(--white);
    white-space: nowrap;
  }
  .tagline {
    position: absolute;
    right: 16px; top: 190px;
    text-align: right;
    color: var(--white);
    font-size: 18px;
    line-height: 1.5;
    text-shadow: 0 1px 2px rgba(0,0,0,0.45);
  }
  .contact {
    position: absolute;
    left: 12px; bottom: 10px;
    list-style: none;
    color: var(--white);
    font-size: 17px;
    line-height: 1.1;
    letter-spacing: -0.3px;
    text-shadow: 0 1px 2px rgba(0,0,0,0.35);
  }
</style>
</head>
<body>

  <section class="card card--front">
    <div class="game-title">Feral Tundra</div>
    <div class="feature-tags">
      <span class="feature-tag">FREE</span>
      <span class="feature-tag">SANDBOX</span>
      <span class="feature-tag">3D Voxel-Based</span>
      <span class="feature-tag">Online Multiplayer</span>
    </div>
    <div class="byline">by Corin Wexford</div>
  </section>

  <section class="card card--back">
    <svg class="screens" viewBox="0 0 945 540" xmlns="http://www.w3.org/2000/svg">
      <defs>
        <linearGradient id="grad-fortress" x1="0" y1="0" x2="0" y2="1">
          <stop offset="0" stop-color="#7b8fa3"/>
          <stop offset="0.55" stop-color="#4b4236"/>
          <stop offset="1" stop-color="#3e5a36"/>
        </linearGradient>
        <linearGradient id="grad-forest" x1="0" y1="0" x2="1" y2="1">
          <stop offset="0" stop-color="#3f5f45"/>
          <stop offset="0.6" stop-color="#5f8060"/>
          <stop offset="1" stop-color="#6c8c8a"/>
        </linearGradient>
        <linearGradient id="grad-bunker" x1="0" y1="0" x2="1" y2="1">
          <stop offset="0" stop-color="#9fdcae"/>
          <stop offset="1" stop-color="#4f8a5c"/>
        </linearGradient>
        <linearGradient id="grad-lake" x1="0" y1="0" x2="0" y2="1">
          <stop offset="0" stop-color="#aebfd2"/>
          <stop offset="0.45" stop-color="#5b6b4b"/>
          <stop offset="1" stop-color="#56718a"/>
        </linearGradient>
      </defs>
      <polygon role="img" aria-label="Game screenshot of a voxel fortress held by chains above mountains" points="0,0 662,0 472,262 440,306 0,306" fill="url(#grad-fortress)"/>
      <polygon role="img" aria-label="Game screenshot of a player with a pistol in a forest clearing" points="674,0 945,0 945,260 488,260" fill="url(#grad-forest)"/>
      <polygon role="img" aria-label="Game screenshot of a green-lit brick bunker interior" points="0,312 436,312 274,540 0,540" fill="url(#grad-bunker)"/>
      <polygon role="img" aria-label="Game screenshot of a lake below wooded mountains" points="478,272 945,272 945,540 282,540" fill="url(#grad-lake)"/>
      <line x1="668" y1="0" x2="480" y2="262" stroke="var(--panel-frame)" stroke-width="7"/>
      <line x1="478" y1="266" x2="945" y2="266" stroke="var(--panel-frame)" stroke-width="7"/>
      <polygon points="945,350 945,540 800,540" fill="var(--corner-black)"/>
    </svg>
    <div class="mini-brand">Feral Tundra</div>
    <p class="tagline">Free Voxel-Based<br>Multiplayer Sandbox Game</p>
    <ul class="contact">
      <li>Name: Corin Wexford</li>
      <li>Position: Lead Developer</li>
      <li>E-mail: Gray_Lanterns@mailnest.example</li>
      <li>Phone number: 555-372-9186</li>
      <li>Website: www.FeralTundra.example</li>
    </ul>
  </section>

</body>
</html>
```